Business Card Design Project

Corwen Property Management

Our Business is residential property management, we therefore need a card that displays a professional image, but is clear and concise, and easy to read
Updates

We are committed now guys and girls, loving what we are seeing so far! 

Target Market(s)

Landlords, Rental Property Owners

Industry/Entity Type

Residential

Requirements
Must have
• Dean Fosterly - Principal
Tessa Fosterly - Director (Property Management)

PO Box 718
Holloway SA 5093

Dean: 0419 372 508
Tessa: 0419 613 947

www.corwenpropertymanagement.com.au
admin@corwenpropertymanagement.com.au

Nice to have
• I would like the card to be double sided, white background on the information side and then colour on the reverse, in blue or black and incorporating our logo

```html
<!DOCTYPE html>
<html lang="en">
<head>
<meta charset="utf-8">
<title>Corwen Property Management – Business Card</title>
<link rel="stylesheet" href="https://fonts.googleapis.com/css2?family=Open+Sans:wght@400;600;700&display=swap">
<style>
  :root {
    --stage: #e9e7e3;
    --card-white: #ffffff;
    --brand-blue: #1a68ad;
    --blue-deep: #0a5aa0;
    --blue-light: #2a8fd6;
    --ink-grey: #4a4b4d;
    --rule-grey: #8a8c8f;
    --text-dark: #333333;
    --white: #ffffff;
  }
  * { box-sizing: border-box; margin: 0; padding: 0; }
  html, body {
    width: 1200px; height: 1015px; overflow: hidden;
    background: var(--stage);
    font-family: "Open Sans", Arial, sans-serif;
  }
  .canvas { position: relative; width: 1200px; height: 1015px; }

  .card {
    position: absolute; width: 734px; height: 418px;
    box-shadow: 0 2px 6px rgba(0,0,0,.18);
    overflow: hidden;
  }
  .card-front { left: 73px; top: 66px; background: var(--card-white); }
  .card-back {
    left: 380px; top: 531px;
    background: radial-gradient(ellipse at 45% 45%, var(--blue-light) 0%, var(--blue-deep) 75%);
  }

  .brand {
    position: absolute; left: 0; right: 0;
    display: flex; align-items: center; justify-content: center; gap: 16px;
    font-weight: 700;
  }
  .brand-mark { width: 30px; height: 30px; border-radius: 3px; flex: none; }
  .brand-text { display: flex; flex-direction: column; line-height: 1; }
  .brand-name { font-size: 74px; letter-spacing: -1px; }
  .brand-sub { font-size: 22px; margin-top: 4px; align-self: flex-end; }

  .card-front .brand { top: 38px; color: var(--ink-grey); }
  .card-front .brand-mark { background: var(--brand-blue); }
  .card-back .brand { top: 160px; color: var(--white); }
  .card-back .brand-mark { background: var(--white); }

  .contacts {
    position: absolute; top: 186px; left: 0; right: 0;
    display: flex; flex-direction: column; align-items: center; gap: 11px;
  }
  .contact-row { display: flex; align-items: baseline; gap: 8px; color: var(--text-dark); font-size: 18px; }
  .contact-name { color: var(--brand-blue); font-weight: 700; font-size: 22px; }
  .contact-divider { width: 1px; height: 20px; background: #b5b5b5; align-self: center; margin: 0 4px; }
  .contact-phone { display: flex; align-items: center; gap: 6px; }
  .icon { width: 13px; height: 13px; fill: currentColor; flex: none; }

  .rule { position: absolute; left: 0; right: 0; height: 3px; background: var(--rule-grey); top: 271px; }
  .info-band {
    position: absolute; left: 0; right: 0; top: 281px; bottom: 0;
    background: linear-gradient(90deg, var(--blue-deep) 0%, var(--brand-blue) 45%, var(--blue-deep) 100%);
    color: var(--white);
    display: flex; flex-direction: column; align-items: center; padding-top: 18px;
    font-size: 19px;
  }
  .info-band .address { margin-bottom: 14px; }
  .info-line { display: flex; align-items: center; gap: 8px; line-height: 1.7; }

  .back-web {
    position: absolute; left: 0; right: 0; top: 330px; text-align: center;
    color: var(--white); font-size: 18px; letter-spacing: 1.6px;
  }
</style>
</head>
<body>
<main class="canvas">

  <section class="card card-front" aria-label="Card front">
    <div class="brand">
      <span class="brand-mark"></span>
      <div class="brand-text">
        <span class="brand-name">Corwen</span>
        <span class="brand-sub">Property Management</span>
      </div>
    </div>

    <div class="contacts">
      <div class="contact-row">
        <span class="contact-name">Dean Fosterly,</span>
        <span class="contact-role">Principal</span>
        <span class="contact-divider"></span>
        <span class="contact-phone">
          <svg class="icon" viewBox="0 0 16 16"><path d="M3.6 1.2l2.3 2.6-1.3 1.8c.9 2 2.3 3.6 4.4 4.7l1.6-1.4 2.8 2.2-1.4 2.6C6.7 13.5 2.3 9 1.1 3.1z"/></svg>
          0419 372 508
        </span>
      </div>
      <div class="contact-row">
        <span class="contact-name">Tessa Fosterly,</span>
        <span class="contact-role">Director</span>
        <span class="contact-divider"></span>
        <span class="contact-phone">
          <svg class="icon" viewBox="0 0 16 16"><path d="M3.6 1.2l2.3 2.6-1.3 1.8c.9 2 2.3 3.6 4.4 4.7l1.6-1.4 2.8 2.2-1.4 2.6C6.7 13.5 2.3 9 1.1 3.1z"/></svg>
          0419 613 947
        </span>
      </div>
    </div>

    <div class="rule"></div>
    <div class="info-band">
      <p class="address">PO Box 718, Holloway SA 5093</p>
      <p class="info-line">
        <svg class="icon" viewBox="0 0 16 16"><path d="M1 3h14v1.2L8 9 1 4.2z"/><path d="M1 5.6l7 4.8 7-4.8V13H1z"/></svg>
        admin@corwenpropertymanagement.com.au
      </p>
      <p class="info-line">
        <svg class="icon" viewBox="0 0 16 16"><circle cx="8" cy="8" r="7"/><path d="M1 8h14M8 1v14" stroke="#1a68ad" stroke-width="1.2"/></svg>
        www.corwenpropertymanagement.com.au
      </p>
    </div>
  </section>

  <section class="card card-back" aria-label="Card back">
    <div class="brand">
      <span class="brand-mark"></span>
      <div class="brand-text">
        <span class="brand-name">Corwen</span>
        <span class="brand-sub">Property Management</span>
      </div>
    </div>
    <p class="back-web">www.corwenpropertymanagement.com.au</p>
  </section>

</main>
</body>
</html>
```